Vorelux - A range of environmental public toilet products

We need a design for an existing company with a new direction. We supply toilet cleaning products, matts etc that not only keep your public toilet clean and smelling good but also clean pipes and toilet bowls at the same time.
Many of the products contain a unique enzyme deodorant formulation, which can effectively kill bacterial, deodorize, eliminating smells and clean the Urinal and pipes with every flush.

The web page needs to say we are clean and sparkeling but please note "THIS IS NOT A HOME PRODUCT but for public urinals and bathrooms.
Our product is not expensive but is helping the environment and
completely safe
Updates

Reason: Unfortunately all members of the comapny are still on holiday and I have not been able to contact 2 of them regarding the site and I would like their input. I think they are all back shortly but not sure.

Target Market(s)

Industrial Cleaners and suppliers to hotels, clubs etc

Industry/Entity Type

Environment

Requirements
Must have
• The front page will have:
Point of Difference
Products
Ordering
Testominials
FAQ
Our Policies
Contact Us
Nice to have
• Make it look like you would want to use the piublic toilets.
As you know public toilets can be ugly places/

```html
<!DOCTYPE html>
<html lang="en">
<head>
<meta charset="utf-8">
<title>Vorelux – Public Washroom Care</title>
<link rel="stylesheet" href="https://fonts.googleapis.com/css2?family=Source+Sans+3:ital,wght@0,400;0,600;0,700;1,700&display=swap">
<style>
:root{
  --blue:#1a4d9c;
  --blue-dark:#14468f;
  --blue-text:#1d57a8;
  --blue-btn:#1f6fc9;
  --blue-btn-dark:#0f4f9e;
  --orange:#f4a225;
  --orange-text:#e3861a;
  --band:#f4f4f4;
  --rule:#c8c8c8;
  --body-text:#4a4a4a;
  --white:#ffffff;
}
*{margin:0;padding:0;box-sizing:border-box}
html,body{width:1091px;height:1200px;overflow:hidden;background:var(--white)}
body{font-family:"Source Sans 3",Arial,sans-serif;color:var(--body-text)}
.page{position:absolute;left:0;top:0;width:1000px;height:1100px;transform:scale(1.091);transform-origin:0 0}
.abs{position:absolute}

/* header */
.header{left:0;top:0;width:1000px;height:362px;background:linear-gradient(180deg,#1b4fa0,#184a96)}
.header-rule{left:0;top:362px;width:1000px;height:4px;background:#5d8fd4}
.brand{left:14px;top:20px;width:300px;height:64px;background:var(--white);border-radius:12px;box-shadow:0 2px 4px rgba(0,0,0,.3);display:flex;align-items:center;padding-left:16px;gap:12px}
.brand-name{font-size:40px;font-weight:700;color:var(--blue);letter-spacing:1px}
.brand-dot{width:14px;height:14px;border-radius:50%;background:var(--orange)}
.nav{left:88px;top:106px;list-style:none}
.nav li{height:32px;display:flex;align-items:center;font-size:15px;color:var(--white)}
.nav li::before{content:"";width:13px;height:13px;border-radius:50%;background:var(--white);margin-right:17px;flex:none}
.nav li.active{color:var(--orange)}
.nav li.active::before{background:var(--orange)}

/* slider */
.slide{left:337px;top:43px;width:617px;height:278px;background:var(--white)}
.slide-caption{left:65px;top:56px;font-size:17px;line-height:24px;color:var(--orange-text);width:320px}
.slide-bottles{left:56px;top:142px;width:148px;height:133px;border-radius:6px;background:linear-gradient(90deg,#6f8fd6,#e77bb1,#e3a1c8,#7aa0e0)}
.slide-bucket{left:393px;top:77px;width:182px;height:198px;border-radius:10px;background:linear-gradient(135deg,#d9472e,#7ccf4a 55%,#6b7fd1)}
.chev{width:30px;height:50px}
.dots{left:569px;top:335px;display:flex;gap:17px}
.dots span{width:14px;height:14px;border-radius:50%;background:var(--white)}
.dots span.on{background:var(--orange)}

/* feature band */
.band{left:0;top:366px;width:1000px;height:226px;background:var(--band)}
.divider{top:386px;width:1px;height:189px;background:var(--rule)}
.icon{width:48px;height:48px;border-radius:6px}
.h-blue{font-size:19px;color:var(--blue-text)}
.order-line{left:0;width:287px;top:463px;text-align:center;font-size:15px;color:#333}
.click{left:46px;top:500px;font-size:13px;color:#333}
.btn{display:flex;align-items:center;justify-content:center;color:var(--white);font-weight:700;border-radius:4px;background:linear-gradient(180deg,var(--blue-btn),var(--blue-btn-dark))}
.btn-order{left:135px;top:493px;width:107px;height:37px;font-size:15px}
.quote-name{left:313px;top:462px;font-size:14px;font-style:italic;font-weight:700;color:#444}
.quote{left:313px;top:490px;width:352px;font-size:13px;line-height:20px;text-align:justify;color:#555}
.quote a{color:var(--blue-text);text-decoration:none}
.label{width:60px;text-align:right;font-size:11px;color:#333}
.field{left:764px;width:193px;height:35px;border:1px solid #c4c4c4;border-radius:6px;background:linear-gradient(180deg,#dcdcdc,#f2f2f2)}
.btn-submit{left:899px;top:550px;width:58px;height:25px;font-size:12px}

/* welcome */
.h-orange{font-size:19px;color:var(--orange-text)}
.copy{left:18px;width:962px;font-size:13px;line-height:20px;text-align:justify;color:var(--body-text)}
.btn-more{left:873px;top:800px;width:106px;height:31px;border-radius:4px;background:var(--orange);color:#333;font-size:13px;display:flex;align-items:center;justify-content:center}
.dashed{left:17px;top:848px;width:963px;border-top:1px dashed #999}

/* products */
.card{top:898px;width:198px;height:108px;border:2px solid #cfcfcf;background:linear-gradient(180deg,#fff,#efefef)}
.card-bottle{position:absolute;left:20px;top:6px;width:44px;height:92px;border-radius:8px 8px 4px 4px;background:linear-gradient(180deg,#2251a8,#e6e9f0 30%,#d33a3a 70%,#e6e9f0)}
.card-title{position:absolute;left:90px;top:14px;font-size:17px;color:var(--blue-text)}
.card .btn{position:absolute;left:87px;width:74px;height:25px;font-size:11px}

/* footer */
.footer{left:0;top:1022px;width:1000px;height:78px;background:var(--blue-dark);border-top:3px solid #4a7cc6}
.footer-links{left:17px;top:1041px;font-size:11px;color:var(--white);display:flex}
.footer-links span+span::before{content:"|";margin:0 10px}
.footer-copy{left:17px;top:1069px;font-size:11px;color:#dfe7f5}
.social{left:829px;top:1048px;display:flex;gap:7px}
.social span{width:24px;height:24px;border-radius:50%;background:var(--white)}
</style>
</head>
<body>
<div class="page">

  <div class="abs header"></div>
  <div class="abs header-rule"></div>

  <div class="abs brand"><span class="brand-name">Vorelux</span><span class="brand-dot"></span></div>

  <ul class="abs nav">
    <li class="active">Point of Difference</li>
    <li>Products</li>
    <li>Ordering</li>
    <li>Testimonials</li>
    <li>FAQ</li>
    <li>Our Policies</li>
    <li>Contact Us</li>
  </ul>

  <div class="abs slide">
    <p class="abs slide-caption">Cicero are also reproduced in their exact original form, accompanied</p>
    <div class="abs slide-bottles" role="img" aria-label="Coloured cleaning spray bottles with pink gloves"></div>
    <div class="abs slide-bucket" role="img" aria-label="Red bucket with green spray bottle, gloves and sponge"></div>
    <svg class="abs chev" style="left:8px;top:115px" viewBox="0 0 30 50"><polyline points="26,4 6,25 26,46" fill="none" stroke="#555" stroke-width="5"/></svg>
    <svg class="abs chev" style="left:573px;top:115px" viewBox="0 0 30 50"><polyline points="4,4 24,25 4,46" fill="none" stroke="#555" stroke-width="5"/></svg>
  </div>

  <div class="abs dots"><span class="on"></span><span></span><span></span><span></span><span></span></div>

  <div class="abs band"></div>
  <div class="abs divider" style="left:287px"></div>
  <div class="abs divider" style="left:693px"></div>

  <div class="abs icon" style="left:22px;top:389px;background:linear-gradient(135deg,#f2f2f2,#c9c9c9)" role="img" aria-label="Order form with pen icon"></div>
  <h2 class="abs h-blue" style="left:85px;top:400px;font-weight:400">Order Now</h2>
  <p class="abs order-line">To keep your toilet Clean and Fresh</p>
  <p class="abs click">Click Here for</p>
  <div class="abs btn btn-order">Order Now</div>

  <div class="abs icon" style="left:328px;top:387px;background:linear-gradient(180deg,#e9b07a,#5a5e66)" role="img" aria-label="Customer icon"></div>
  <h2 class="abs h-blue" style="left:389px;top:400px;font-weight:400">Testimonials</h2>
  <p class="abs quote-name">Marcus</p>
  <p class="abs quote">“This cleansing product combines Surfactant, Deodorizer, Aromatics and other clean Natural ingredients, that not only cleanse but also sterilize. ” <a href="#">View more</a></p>

  <div class="abs icon" style="left:728px;top:392px;background:linear-gradient(135deg,#e8eef8,#9fb4d6)" role="img" aria-label="Envelope icon"></div>
  <h2 class="abs h-blue" style="left:796px;top:400px;font-weight:400">News Letter</h2>
  <p class="abs label" style="left:694px;top:472px">Name :</p>
  <div class="abs field" style="top:462px"></div>
  <p class="abs label" style="left:694px;top:516px">Email :</p>
  <div class="abs field" style="top:506px"></div>
  <div class="abs btn btn-submit">SUBMIT</div>

  <h2 class="abs h-orange" style="left:17px;top:607px;font-weight:400">Welcome To Vorelux</h2>
  <p class="abs copy" style="top:646px">These Toilet discs contain a unique enzyme deodorant formulation, which can effectively kill bacterial, deodorize, eliminating smells and clean the Urinal and pipes with every flush. The triangle shaped screen is designed to help prevent drains from getting clogged. The blocks contain a unique formula of Enzymes thatcan not only clean but effectively control the disbursement and will last up to 500 flushes.</p>
  <p class="abs copy" style="top:726px">These Urinal screens contain special built-in anti-bacterial ingredients and natural fragrances. They are uniquely design to promote strong flushing with one size fitting most urinals and prevent clogging of drains and hence costly repairs. They also have a long lasting fragrance embedded in the material and are environmentally friendly andnon-toxic. They will last between30-45 days with constant use</p>
  <div class="abs btn-more">Read more...</div>
  <div class="abs dashed"></div>

  <h2 class="abs h-orange" style="left:17px;top:857px;font-weight:400">Our Products</h2>
  <svg class="abs" style="left:26px;top:935px" width="20" height="30" viewBox="0 0 20 30"><polyline points="16,3 4,15 16,27" fill="none" stroke="#888" stroke-width="3"/></svg>
  <svg class="abs" style="left:941px;top:935px" width="20" height="30" viewBox="0 0 20 30"><polyline points="4,3 16,15 4,27" fill="none" stroke="#888" stroke-width="3"/></svg>

  <div class="abs card" style="left:64px"><div class="card-bottle" role="img" aria-label="Toilet cleaner bottle"></div><span class="card-title">Chem 01</span><div class="btn" style="top:40px">View more</div><div class="btn" style="top:69px">Buy Now</div></div>
  <div class="abs card" style="left:285px"><div class="card-bottle" role="img" aria-label="Toilet cleaner bottle"></div><span class="card-title">Chem 02</span><div class="btn" style="top:40px">View more</div><div class="btn" style="top:69px">Buy Now</div></div>
  <div class="abs card" style="left:506px"><div class="card-bottle" role="img" aria-label="Toilet cleaner bottle"></div><span class="card-title">Chem 03</span><div class="btn" style="top:40px">View more</div><div class="btn" style="top:69px">Buy Now</div></div>
  <div class="abs card" style="left:727px"><div class="card-bottle" role="img" aria-label="Toilet cleaner bottle"></div><span class="card-title">Chem 04</span><div class="btn" style="top:40px">View more</div><div class="btn" style="top:69px">Buy Now</div></div>

  <div class="abs footer"></div>
  <div class="abs footer-links"><span>Home</span><span>Point of Difference</span><span>Products</span><span>Ordering</span><span>Testiminials</span><span>FAQ</span><span>Our Policies</span><span>Contact Us</span><span>Sitemap</span></div>
  <p class="abs footer-copy">Copyright © 2011 www.vorelux.com &nbsp; All rights reserved</p>
  <div class="abs social"><span></span><span></span><span></span><span></span><span></span></div>

</div>
</body>
</html>
```